Amazing new protein bar on the market - be a part of something special

We need packaging design for the wrapper for great tasting new protein. The product is called "Copperleaf Crisp". The packaging should have a modern font and design I catching - Copperleaf Crisp. If possible we would like to incorporate a picture of the bar in the background. The font and name of the bar should stand out and jump out at you. Modern font is a must. The product run will be blueberry - pomegranate. Please use bright colors, White, Red and/or Orange. Lightning bolts would be a plus.
Updates

Project Deadline Extended Reason: We have changed our product name. Would like to see more designs. Added Monday, April 17, 2017

Target Market(s)

Athletes, people on the go or on a diet

Industry/Entity Type

Product

Logo Text

Copperleaf Crisp

Colors
f04a51
f68e4e
faa54b
ffffff

Requirements
Must have
• Prefer modern font that jumps out at you. Slanted if possible
• Please use bright colors White, Red and/or Orange

```html
<!DOCTYPE html>
<html lang="en">
<head>
<meta charset="utf-8">
<title>Copperleaf Crisp – Wrapper</title>
<link rel="stylesheet" href="https://fonts.googleapis.com/css2?family=Russo+One&family=Open+Sans:wght@600&display=swap">
<style>
  :root{
    --bg:#ffffff;
    --orange:#f0620f;
    --orange-deep:#e2520a;
    --orange-light:#f68e4e;
    --amber:#faa54b;
    --panel:#ffffff;
    --panel-shade:#eef0f2;
    --brown:#4a1a0c;
    --label:#e0610f;
  }
  html,body{margin:0;padding:0;overflow:hidden;background:var(--bg);}
  .canvas{width:1200px;height:857px;position:relative;background:var(--bg);}
  .wrapper{position:absolute;left:0;top:0;}
  .product-name{font-family:"Russo One",sans-serif;fill:var(--brown);}
  .benefit{font-family:"Open Sans",sans-serif;font-weight:600;font-size:12.5px;fill:var(--label);letter-spacing:.2px;}
  .icon{fill:none;stroke:var(--label);stroke-width:2.2;stroke-linecap:round;stroke-linejoin:round;}
</style>
</head>
<body>
<div class="canvas">
  <svg class="wrapper" width="1200" height="857" viewBox="0 0 1200 857" xmlns="http://www.w3.org/2000/svg">
    <defs>
      <linearGradient id="wrapFill" x1="0" y1="0" x2="0" y2="1">
        <stop offset="0" stop-color="var(--orange-deep)"/>
        <stop offset=".5" stop-color="var(--orange)"/>
        <stop offset="1" stop-color="var(--orange-deep)"/>
      </linearGradient>
      <linearGradient id="panelFill" x1="0" y1="0" x2="1" y2="1">
        <stop offset="0" stop-color="var(--panel)"/>
        <stop offset="1" stop-color="var(--panel-shade)"/>
      </linearGradient>
      <linearGradient id="barPhoto" x1="0" y1="0" x2="1" y2="1">
        <stop offset="0" stop-color="#e9c08a"/>
        <stop offset=".55" stop-color="#c98a4e"/>
        <stop offset="1" stop-color="#f3ece4"/>
      </linearGradient>
      <linearGradient id="ghostBar" x1="0" y1="0" x2="1" y2="0">
        <stop offset="0" stop-color="#d8571a" stop-opacity="0"/>
        <stop offset="1" stop-color="#c9531c" stop-opacity=".6"/>
      </linearGradient>
    </defs>

    <!-- wrapper body with crimped ends -->
    <path fill="url(#wrapFill)" d="M124 262 L1062 262 L1062 628 L124 628 Z"/>
    <g fill="var(--bg)">
      <path d="M124 262 l6 9 -6 9 6 9 -6 9 6 9 -6 9 6 9 -6 9 6 9 -6 9 6 9 -6 9 6 9 -6 9 6 9 -6 9 6 9 -6 9 6 9 -6 9 6 9 -6 9 6 9 -6 9 6 9 -6 9 6 9 -6 9 6 9 -6 9 6 9 -6 9 6 9 -6 9 6 9 -6 9 6 9 -6 9 6 9 -6 6 Z"/>
      <path d="M1062 262 l-6 9 6 9 -6 9 6 9 -6 9 6 9 -6 9 6 9 -6 9 6 9 -6 9 6 9 -6 9 6 9 -6 9 6 9 -6 9 6 9 -6 9 6 9 -6 9 6 9 -6 9 6 9 -6 9 6 9 -6 9 6 9 -6 9 6 9 -6 9 6 9 -6 9 6 9 -6 9 6 9 -6 9 6 9 -6 9 6 9 -6 9 6 6 Z"/>
    </g>

    <!-- faint background bar on left end -->
    <rect role="img" aria-label="Faded photo of the blueberry pomegranate bar" x="190" y="420" width="200" height="120" rx="20" fill="url(#ghostBar)"/>

    <!-- white label panel -->
    <polygon class="label-panel" fill="url(#panelFill)" points="412,285 936,285 888,606 364,606"/>

    <!-- product name -->
    <text class="product-name" transform="translate(420 410) skewX(-10)" x="0" y="0" font-size="74" textLength="468" lengthAdjust="spacingAndGlyphs">COPPERLEAF</text>
    <text class="product-name" transform="translate(598 512) skewX(-10)" x="0" y="0" font-size="86" textLength="272" lengthAdjust="spacingAndGlyphs">CRISP</text>

    <!-- bar photo -->
    <rect role="img" aria-label="Photo of the crisp bar with white drizzle, blueberries and pomegranate seeds" x="384" y="428" width="184" height="104" rx="10" fill="url(#barPhoto)"/>

    <!-- benefits -->
    <g class="benefits">
      <g transform="translate(394 573)">
        <circle class="icon" r="13"/><circle class="icon" r="7.5"/><circle class="icon" r="2.5"/>
        <path class="icon" d="M2 -2 L14 -14 M10 -14 h4 v4"/>
      </g>
      <text class="benefit" x="427" y="569">ENHANCED MEMORY</text>
      <text class="benefit" x="427" y="585">&amp; MENTAL SHARPNESS</text>

      <g transform="translate(593 573)">
        <circle class="icon" r="13"/>
        <path class="icon" d="M-6 5 q0 -10 6 -11 q5 0 4 5 q4 -2 5 3 q0 5 -6 5 h-7 z"/>
      </g>
      <text class="benefit" x="616" y="569">PROMOTES</text>
      <text class="benefit" x="616" y="585">WEIGHT LOSS</text>

      <g transform="translate(760 573)">
        <circle class="icon" r="12"/>
        <path class="icon" d="M0 -7 V0 L5 4"/>
        <path class="icon" d="M-16 -6 h-10 M-16 0 h-14 M-16 6 h-10"/>
      </g>
      <text class="benefit" x="783" y="569">ENDURANCE</text>
      <text class="benefit" x="783" y="585">ENHANCEMENT</text>
    </g>
  </svg>
</div>
</body>
</html>
```